Beer Garden Specials socials

Hello - simular to last project but for a different venue.

Specials are:
$5 @ 5pm - $5 Pints Wednesday - Sunday.
Wednesday $1 Chicken Wings
Thursday - $12.50 Pizzas
Friday $12.48 Pint & Burger 12-3pm
Kids Eat Free - Saturdays & Sundays 12-3pm

Need an instagram image for each special and also a combined Facebook cover.
Needs to be classy but playful

```html
<!DOCTYPE html>
<html lang="en">
<head>
<meta charset="utf-8">
<title>Hopyard Taproom – Weekly Specials Socials</title>
<link rel="stylesheet" href="https://fonts.googleapis.com/css2?family=Passion+One:wght@400;700&family=Alfa+Slab+One&display=swap">
<style>
  :root {
    --board: #ededed;
    --ink: #111111;
    --white: #ffffff;
    --pints-bg: #ff3a0a;
    --wings-bg: #a32224;
    --pizza-bg: #ff5c5c;
    --burger-bg: #7a3320;
    --kids-bg: #e60a35;
    --strip-cream: #fff1b8;
    --strip-red: #dc0a3a;
    --strip-rule: #e8788a;
    --amber: #f7b51c;
    --orange: #f28a1e;
    --head: "Passion One", "Arial Narrow", sans-serif;
    --slab: "Alfa Slab One", Georgia, serif;
  }
  * { box-sizing: border-box; margin: 0; padding: 0; }
  html, body { width: 1200px; height: 1200px; overflow: hidden; }
  body { background: var(--board); position: relative; font-family: var(--head); }

  .tile {
    position: absolute;
    width: 318px; height: 318px;
    background: var(--tile-bg);
    box-shadow: 0 8px 18px rgba(0,0,0,.28);
    text-align: center;
  }
  .tile--pints  { --tile-bg: var(--pints-bg);  left: 65px;  top: 101px; }
  .tile--wings  { --tile-bg: var(--wings-bg);  left: 438px; top: 101px; }
  .tile--pizza  { --tile-bg: var(--pizza-bg);  left: 817px; top: 101px; }
  .tile--burger { --tile-bg: var(--burger-bg); left: 257px; top: 470px; }
  .tile--kids   { --tile-bg: var(--kids-bg);   left: 632px; top: 470px; }

  .offer {
    position: absolute; left: 84px; top: 20px;
    width: 146px; height: 98px;
    border: 2px dotted var(--white);
    display: flex; flex-direction: column; align-items: center; justify-content: center;
    padding-top: 6px;
  }
  .offer--tall { height: 107px; }
  .offer__day {
    position: absolute; top: -8px; left: 50%; transform: translateX(-50%);
    background: var(--tile-bg);
    padding: 0 4px;
    font-size: 12px; font-weight: 400; letter-spacing: .2px;
    color: var(--ink); white-space: nowrap; line-height: 14px;
  }
  .offer__price { font-size: 34px; font-weight: 700; color: var(--white); line-height: 30px; }
  .offer__title { font-size: 52px; font-weight: 700; color: var(--ink); line-height: 42px; text-transform: uppercase; }
  .offer__title--stack { font-size: 40px; line-height: 32px; }
  .offer__lead { font-size: 38px; font-weight: 700; color: var(--white); line-height: 34px; }

  .tile__art {
    position: absolute; left: 50%; transform: translateX(-50%);
    border-radius: 10px;
  }
  .art--mug   { top: 131px; width: 50px; height: 58px; background: linear-gradient(180deg, var(--white) 0 22%, var(--amber) 22%); border: 2px solid var(--ink); }
  .art--wings { top: 148px; width: 62px; height: 58px; background: linear-gradient(135deg, var(--orange), var(--amber)); border: 2px solid var(--ink); }
  .art--pizza { top: 142px; width: 56px; height: 66px; background: linear-gradient(160deg, var(--orange), #ffd75a); border: 2px solid var(--ink); }
  .art--combo { top: 150px; width: 154px; height: 58px; background: linear-gradient(90deg, var(--amber) 0 32%, transparent 32% 68%, var(--orange) 68%); border-radius: 10px; }
  .art--kids  { top: 130px; width: 70px; height: 62px; background: linear-gradient(135deg, var(--amber), #ffe45c); border: 2px solid var(--ink); border-radius: 30px; }

  .tile__time {
    position: absolute; left: 0; right: 0; top: 200px;
    font-family: var(--slab); font-size: 19px; color: var(--white); letter-spacing: 1px;
  }

  .brand {
    position: absolute; left: 50%; top: 255px; transform: translateX(-50%);
    display: flex; align-items: center; gap: 6px;
    font-family: var(--head); font-weight: 700; font-size: 17px; letter-spacing: 1px;
    color: var(--ink); white-space: nowrap;
  }
  .brand__square { width: 12px; height: 12px; background: var(--ink); }

  .cover {
    position: absolute; left: 255px; top: 836px;
    width: 695px; height: 257px;
    background: var(--strip-cream);
    box-shadow: 0 8px 18px rgba(0,0,0,.22);
    overflow: hidden;
  }
  .cover__band { position: absolute; inset: 0; width: 695px; height: 257px; }
  .cover__frame {
    position: absolute; left: 22px; top: 21px; width: 650px; height: 216px;
    border: 2px dotted var(--ink);
    display: grid;
    grid-template-columns: 150px 121px 110px 117px 1fr;
  }
  .special { position: relative; text-align: center; color: var(--ink); }
  .special + .special { border-left: 2px dotted var(--strip-rule); }
  .special > * { position: absolute; left: 0; right: 0; }
  .special__day   { top: 14px;  font-size: 13px; white-space: nowrap; }
  .special__price { top: 36px;  font-size: 22px; font-weight: 700; }
  .special__time  { top: 74px;  font-size: 15px; font-weight: 700; }
  .special__title { top: 104px; font-size: 22px; font-weight: 700; line-height: 21px; text-transform: uppercase; }
  .special__art   { top: 166px; left: 50%; right: auto; transform: translateX(-50%); height: 30px; border-radius: 6px; border: 1.5px solid var(--ink); }
  .special__art--mug   { width: 24px; background: linear-gradient(180deg, var(--white) 0 24%, var(--amber) 24%); }
  .special__art--wings { width: 30px; background: linear-gradient(135deg, var(--orange), var(--amber)); }
  .special__art--pizza { width: 26px; background: linear-gradient(160deg, var(--orange), #ffd75a); }
  .special__art--combo { width: 80px; border: none; background: linear-gradient(90deg, var(--amber) 0 32%, transparent 32% 64%, var(--orange) 64%); }
  .special__art--kids  { width: 40px; border-radius: 16px; background: linear-gradient(135deg, var(--amber), #ffe45c); }
</style>
</head>
<body>

  <section class="tile tile--pints">
    <div class="offer">
      <span class="offer__day">WEDNESDAY – SUNDAY</span>
      <span class="offer__price">$5</span>
      <span class="offer__title">PINTS</span>
    </div>
    <div class="tile__art art--mug" role="img" aria-label="Illustration of a frothy beer mug"></div>
    <p class="tile__time">5PM</p>
    <div class="brand"><span class="brand__square"></span>HOPYARD</div>
  </section>

  <section class="tile tile--wings">
    <div class="offer offer--tall">
      <span class="offer__day">WEDNESDAY</span>
      <span class="offer__price">$1</span>
      <span class="offer__title offer__title--stack">CHICKEN<br>WINGS</span>
    </div>
    <div class="tile__art art--wings" role="img" aria-label="Illustration of two chicken drumsticks"></div>
    <div class="brand"><span class="brand__square"></span>HOPYARD</div>
  </section>

  <section class="tile tile--pizza">
    <div class="offer">
      <span class="offer__day">THURSDAY</span>
      <span class="offer__price">$12.50</span>
      <span class="offer__title">PIZZAS</span>
    </div>
    <div class="tile__art art--pizza" role="img" aria-label="Illustration of a pepperoni pizza slice"></div>
    <div class="brand"><span class="brand__square"></span>HOPYARD</div>
  </section>

  <section class="tile tile--burger">
    <div class="offer offer--tall">
      <span class="offer__day">FRIDAY</span>
      <span class="offer__price">$12.48</span>
      <span class="offer__title offer__title--stack">PINT+<br>BURGER</span>
    </div>
    <div class="tile__art art--combo" role="img" aria-label="Illustration of a beer mug plus a cheeseburger"></div>
    <div class="brand"><span class="brand__square"></span>HOPYARD</div>
  </section>

  <section class="tile tile--kids">
    <div class="offer offer--tall">
      <span class="offer__day">SATURDAYS &amp; SUNDAYS</span>
      <span class="offer__lead">KIDS EAT</span>
      <span class="offer__title">FREE</span>
    </div>
    <div class="tile__art art--kids" role="img" aria-label="Illustration of two happy children"></div>
    <p class="tile__time">12-3PM</p>
    <div class="brand"><span class="brand__square"></span>HOPYARD</div>
  </section>

  <section class="cover">
    <svg class="cover__band" viewBox="0 0 695 257" aria-hidden="true">
      <path fill="#dc0a3a" d="M300 0 C272 26 290 40 262 62 C234 84 250 100 222 122 C194 144 210 160 182 182 C154 204 168 222 140 240 L117 257 L394 257 C420 232 404 218 432 196 C460 174 444 158 472 136 C500 114 484 98 512 76 C540 54 524 38 552 16 L577 0 Z"/>
    </svg>
    <div class="cover__frame">
      <div class="special">
        <span class="special__day">WEDNESDAY – SUNDAY</span>
        <span class="special__price">$5</span>
        <span class="special__time">@ 5pm</span>
        <span class="special__title">PINTS</span>
        <span class="special__art special__art--mug" role="img" aria-label="Beer mug illustration"></span>
      </div>
      <div class="special">
        <span class="special__day">WEDNESDAY</span>
        <span class="special__price">$1</span>
        <span class="special__title">CHICKEN<br>WINGS</span>
        <span class="special__art special__art--wings" role="img" aria-label="Chicken wings illustration"></span>
      </div>
      <div class="special">
        <span class="special__day">THURSDAY</span>
        <span class="special__price">$12.50</span>
        <span class="special__title">PIZZAS</span>
        <span class="special__art special__art--pizza" role="img" aria-label="Pizza slice illustration"></span>
      </div>
      <div class="special">
        <span class="special__day">FRIDAY</span>
        <span class="special__price">$12.48</span>
        <span class="special__time">12-3pm</span>
        <span class="special__title">PINT+<br>BURGER</span>
        <span class="special__art special__art--combo" role="img" aria-label="Beer mug plus burger illustration"></span>
      </div>
      <div class="special">
        <span class="special__day">SATURDAYS &amp; SUNDAYS</span>
        <span class="special__time">12-3pm</span>
        <span class="special__title">KIDS EAT<br>FREE</span>
        <span class="special__art special__art--kids" role="img" aria-label="Two happy children illustration"></span>
      </div>
    </div>
  </section>

</body>
</html>
```